Cafe - A FRAME Design

Need to create an A frame for my café.
Logo available
Word document - has basic information we think would be good.

Name: Brovvle Café

Notes from the A-frame printers.
File Requirements
• PDF without trim, crop or registration marks
• All files to be CMYK, not RGB
• All fonts converted to outlines (paths/curves)
• Embed all images and elements
• Files to be 100% scale unless otherwise specified
• 10mm Bleed
Resolution
• Bitmap images no less than 130 DPI at full size
Pantone Colours
• If required Pantone colours must be supplied

Target Market(s)

Mainly Students - University cafe

Requirements
Must have
• Cafe name: Brovvle
Nice to have
• Might be nice to have background - that orange color same as logo - just an idea

Word document - has basic idea regarding text that should be included

```html
<!DOCTYPE html>
<html lang="en">
<head>
<meta charset="utf-8">
<title>Brovvle Café – A-Frame Sign</title>
<link rel="stylesheet" href="https://fonts.googleapis.com/css2?family=Arvo:wght@400;700&family=Yellowtail&display=swap">
<style>
  :root {
    --page-bg: #e9e7e4;
    --bean-dark: #2a1710;
    --bean-mid: #4a2c1d;
    --bean-light: #6b4430;
    --brand-orange: #ec5a12;
    --cream: #ffffff;
  }
  * { margin: 0; padding: 0; box-sizing: border-box; }
  html, body {
    width: 1200px;
    height: 799px;
    overflow: hidden;
    background: var(--page-bg);
  }
  .canvas {
    width: 1200px;
    height: 799px;
    display: flex;
    align-items: center;
    justify-content: center;
  }
  .a-frame-panel {
    width: 442px;
    height: 760px;
    display: block;
    box-shadow: 0 6px 20px rgba(0,0,0,0.18);
  }
  .slab { font-family: "Arvo", Georgia, serif; fill: var(--cream); }
  .script { font-family: "Yellowtail", "Brush Script MT", cursive; fill: var(--cream); }
</style>
</head>
<body>
<main class="canvas">
  <svg class="a-frame-panel" viewBox="0 0 442 760" xmlns="http://www.w3.org/2000/svg">
    <defs>
      <radialGradient id="beanTone" cx="50%" cy="45%" r="75%">
        <stop offset="0%" stop-color="var(--bean-light)"/>
        <stop offset="55%" stop-color="var(--bean-mid)"/>
        <stop offset="100%" stop-color="var(--bean-dark)"/>
      </radialGradient>
    </defs>

    <rect class="bean-backdrop" role="img" aria-label="Photo of roasted coffee beans filling the background"
          x="0" y="0" width="442" height="760" fill="url(#beanTone)"/>

    <rect class="info-panel" x="30" y="100" width="382" height="596" rx="22" fill="var(--brand-orange)"/>

    <!-- brand -->
    <circle class="brand-dot" cx="100" cy="190" r="24" fill="var(--cream)"/>
    <text class="slab brand-name" x="50" y="292" font-size="36" font-weight="400">Brovvle</text>

    <!-- tagline -->
    <text class="script tagline-lead" x="226" y="238" font-size="32">Your</text>
    <line class="divider" x1="232" y1="252" x2="232" y2="318" stroke="var(--cream)" stroke-width="1.5"/>
    <g class="slab tagline" font-size="14" font-weight="700">
      <text x="242" y="268">environmentally</text>
      <text x="242" y="290">&amp; sustainability</text>
      <text x="242" y="312">focused café</text>
    </g>

    <g class="slab headline" font-weight="700" font-size="48">
      <text x="96" y="420">Specialty</text>
      <text x="334" y="474" text-anchor="end">Coffee</text>
    </g>

    <g class="slab offer" font-size="16">
      <text x="92" y="516">Fresh Food, Pastries &amp; Drinks</text>
      <text x="92" y="540"><tspan font-weight="700">(Vegan &amp; GF)</tspan> options available</text>
    </g>

    <text class="slab catering" x="221" y="596" text-anchor="middle" font-size="13.5"
          font-weight="700" letter-spacing="1.2">CATERING AVAILABLE</text>

    <text class="slab location" x="221" y="664" text-anchor="middle" font-size="12"
          font-weight="700">Located @ Building 118</text>
  </svg>
</main>
</body>
</html>
```